Business Intelligence / Data Visualization Firm Seeking World Class Power Point Deck

Kestrel Arc delivers enterprise business intelligence and data visualization solutions enabling clients to see their business as they've never seen it - we transform complex, unstructured data into simple insight that facilitates intelligent decision making, revenue growth and risk reduction. We're seeking a world class power point template for internal, client and conference presentations.

Please visit kestrelarc.net for more company context.
*Note: A website photo has been uploaded and may be used or not used - designer discretion.

Additional context:
We use Quillmark: https://quillmark.brenvoda.com/products/predictive-analytics.

Target Market(s)

CXOs at Merivale 100 companies | small and medium business owners (BI / data-viz experts and also decision makers who don't actually understand BI / data-viz).

Industry/Entity Type

Professional Service

Font styles to use
Sans Serif
Other font styles liked:
• Our logo is Expansiva (uploaded), our site is Tahoma. Please use your discretion,.

Colors
ec1f27
ffffff
000000

Requirements
Must have
• PPT format, editable.
• Prefer simple, clean, strong presentation.
Nice to have
• Designs that relate to data, analytics, solutions, automation and transforming complexity into simplicity.
• Reusable icons.

```html
<!DOCTYPE html>
<html lang="en">
<head>
<meta charset="utf-8">
<title>Revised Slide Design Data Display Ideas</title>
<link rel="stylesheet" href="https://fonts.googleapis.com/css2?family=Michroma&family=Open+Sans:ital,wght@0,400;0,600;0,700;1,400&family=Roboto:wght@700&display=swap">
<style>
  :root{
    --red:#ec1f27;
    --red-soft:#d83a3f;
    --black:#000000;
    --ink:#1c1c1c;
    --charcoal:#2b2b2b;
    --navy:#2e3b52;
    --white:#ffffff;
    --grey:#7a7a7a;
    --grey-light:#bdbdbd;
    --band:#8d7d64;
    --page:#ffffff;
  }
  *{box-sizing:border-box;margin:0;padding:0}
  html,body{width:1200px;height:1200px;overflow:hidden;background:var(--page)}
  .sheet{position:relative;width:1200px;height:1200px}
  .sheet-title{position:absolute;top:140px;left:0;width:1200px;text-align:center;
    font-family:'Roboto',sans-serif;font-weight:700;font-size:35px;letter-spacing:.5px;color:#7b7b7b}
  .showcase{position:absolute;top:262px;left:0;width:1200px;height:676px;background:var(--band)}
  .slide{position:absolute;width:320px;height:180px;box-shadow:0 3px 8px rgba(0,0,0,.35);background:var(--white);overflow:hidden}
  .slide svg{display:block;width:320px;height:180px}
  .c1{left:70px}.c2{left:445px}.c3{left:819px}
  .r1{top:294px}.r2{top:501px}.r3{top:712px}
  .hd{font-family:'Michroma',sans-serif;font-size:10px;fill:var(--ink)}
  .hd-w{font-family:'Michroma',sans-serif;fill:var(--white)}
  .logo{font-family:'Michroma',sans-serif;font-size:6px;fill:var(--white);letter-spacing:.4px}
  .logo-dark{font-family:'Michroma',sans-serif;fill:var(--ink);letter-spacing:.2px}
  .foot{font-family:'Michroma',sans-serif;font-size:3.6px;fill:var(--white);letter-spacing:.6px}
  .sub{font-family:'Open Sans',sans-serif;font-size:3.2px;fill:#8a8a8a}
  .p{font-family:'Open Sans',sans-serif;font-style:italic;font-size:3.5px;fill:#666}
  .pw{font-family:'Open Sans',sans-serif;font-size:3.5px;fill:var(--white)}
  .pw-t{font-family:'Open Sans',sans-serif;font-weight:700;font-size:4px;fill:var(--white)}
  .pw-s{font-family:'Open Sans',sans-serif;font-size:3.1px;fill:var(--white)}
  .it{font-family:'Open Sans',sans-serif;font-weight:600;font-size:5px;fill:#444}
  .it-s{font-family:'Open Sans',sans-serif;font-weight:600;font-size:3.8px;fill:#444}
  .itb{font-family:'Open Sans',sans-serif;font-weight:700;font-size:5px;fill:var(--ink)}
  .sm{font-family:'Open Sans',sans-serif;font-size:3.1px;fill:#777}
  .ax{font-family:'Open Sans',sans-serif;font-size:4px;fill:#555}
  .ax-s{font-family:'Open Sans',sans-serif;font-size:3.4px;fill:#333}
  .ct{font-family:'Open Sans',sans-serif;font-size:5px;fill:#555}
  .lf{font-family:'Open Sans',sans-serif;font-size:4px;fill:var(--white)}
  .num{font-family:'Open Sans',sans-serif;font-weight:700;font-size:4.5px}
  .num-s{font-family:'Open Sans',sans-serif;font-weight:700;font-size:3.8px;fill:var(--white)}
</style>
</head>
<body>
<main class="sheet">
  <h1 class="sheet-title">REVISED SLIDE DESIGN DATA DISPLAY IDEAS</h1>
  <div class="showcase"></div>

  <!-- Slide: monthly bar chart -->
  <section class="slide c1 r1">
    <svg viewBox="0 0 400 225">
      <rect width="400" height="225" fill="#fff"/>
      <rect x="0" y="9" width="4" height="11" fill="var(--red)"/>
      <text class="hd" x="11" y="18">YOUR TITLE HERE</text>
      <text class="sub" x="11" y="26">Enter your subtitle here</text>
      <rect x="311" y="5" width="83" height="12" fill="var(--black)"/>
      <text class="logo" x="352.5" y="13.3" text-anchor="middle">KESTREL ARC</text>
      <text class="p" x="25" y="45">Kestrel Arc turns complex data into simple insight for leaders who need clear answers fast, and helps every team see the business</text>
      <text class="p" x="25" y="52">plainly. Dashboards, models and reports work together so that decisions rest on facts, growth is planned and risk is reduced at every</text>
      <text class="p" x="25" y="59">level of the company, from the board room to the shop floor.</text>
      <text class="ct" x="86" y="87" text-anchor="middle">Monthly</text>
      <g class="ax" text-anchor="end">
        <text x="35" y="97.5">10</text><text x="35" y="111.5">8</text><text x="35" y="125.5">6</text>
        <text x="35" y="139.5">4</text><text x="35" y="153.5">2</text><text x="35" y="167.5">0</text>
      </g>
      <line x1="40" y1="166" x2="138" y2="166" stroke="#ccc" stroke-width=".5"/>
      <rect x="50" y="146.4" width="13" height="19.6" fill="var(--black)"/>
      <rect x="50" y="126.1" width="13" height="20.3" fill="var(--red)"/>
      <rect x="84" y="146.4" width="13" height="19.6" fill="var(--black)"/>
      <rect x="84" y="111.4" width="13" height="35" fill="var(--red)"/>
      <rect x="118" y="138" width="13" height="28" fill="var(--black)"/>
      <rect x="118" y="102.3" width="13" height="35.7" fill="var(--red)"/>
      <g class="ax" text-anchor="middle"><text x="56.5" y="174">Apr</text><text x="90.5" y="174">May</text><text x="124.5" y="174">Jun</text></g>
      <rect x="60" y="179" width="3" height="3" fill="var(--black)"/><text class="ax" x="64.5" y="182">Series 1</text>
      <rect x="90" y="179" width="3" height="3" fill="var(--red)"/><text class="ax" x="94.5" y="182">Series 2</text>
      <g>
        <circle cx="179" cy="105" r="11" fill="var(--red)"/><circle cx="179" cy="105" r="8" fill="none" stroke="#fff" stroke-width=".6"/>
        <ellipse cx="179" cy="101" rx="4" ry="1.5" fill="none" stroke="#fff" stroke-width=".8"/>
        <path d="M175 101v7c0 2 8 2 8 0v-7M175 104.5c0 2 8 2 8 0" fill="none" stroke="#fff" stroke-width=".8"/>
        <text class="it" x="197" y="101">Title Goes Here</text>
        <text class="sm" x="199" y="108">Suitable for all categories business</text>
        <text class="sm" x="199" y="114">and personal presentation</text>
      </g>
      <g>
        <circle cx="294" cy="105" r="11" fill="var(--red)"/><circle cx="294" cy="105" r="8" fill="none" stroke="#fff" stroke-width=".6"/>
        <path d="M294 99l6 3-6 3-6-3zM288 105l6 3 6-3M288 108l6 3 6-3" fill="none" stroke="#fff" stroke-width=".8"/>
        <text class="it" x="315" y="101">Title Goes Here</text>
        <text class="sm" x="317" y="108">Suitable for all categories business</text>
        <text class="sm" x="317" y="114">and personal presentation</text>
      </g>
      <g>
        <circle cx="179" cy="155" r="11" fill="var(--red)"/><circle cx="179" cy="155" r="8" fill="none" stroke="#fff" stroke-width=".6"/>
        <path d="M175 149h6l3 3v9h-9z" fill="none" stroke="#fff" stroke-width=".8"/>
        <path d="M177 159v-3M179 159v-5M181 159v-2" stroke="#fff" stroke-width=".9"/>
        <text class="it" x="197" y="151">Title Goes Here</text>
        <text class="sm" x="199" y="158">Suitable for all categories business</text>
        <text class="sm" x="199" y="164">and personal presentation</text>
      </g>
      <g>
        <circle cx="294" cy="155" r="11" fill="var(--red)"/><circle cx="294" cy="155" r="8" fill="none" stroke="#fff" stroke-width=".6"/>
        <path d="M289 160h10M290.5 159v-4M293 159v-7M295.5 159v-5M298 159v-8" stroke="#fff" stroke-width="1.3"/>
        <text class="it" x="315" y="151">Title Goes Here</text>
        <text class="sm" x="317" y="158">Suitable for all categories business</text>
        <text class="sm" x="317" y="164">and personal presentation</text>
      </g>
      <rect x="0" y="216" width="400" height="9" fill="var(--black)"/>
      <text class="foot" x="10" y="222">KESTRELARC.NET</text>
    </svg>
  </section>

  <!-- Slide: dark header with grouped bars -->
  <section class="slide c2 r1">
    <svg viewBox="0 0 400 225">
      <defs>
        <linearGradient id="darkHead" x1="0" y1="0" x2="1" y2="1">
          <stop offset="0" stop-color="#0c1216"/><stop offset="1" stop-color="#163036"/>
        </linearGradient>
      </defs>
      <rect width="400" height="225" fill="#fff"/>
      <rect width="400" height="80" fill="url(#darkHead)"/>
      <text class="hd-w" x="182" y="23" font-size="12" text-anchor="middle">YOUR TITLE HERE</text>
      <text class="logo" x="391" y="13" text-anchor="end">KESTREL ARC</text>
      <text class="pw" x="25" y="40" font-style="italic">Kestrel Arc turns complex data into simple insight for leaders who need clear answers fast, and helps every</text>
      <text class="pw" x="25" y="46" font-style="italic">team see the business plainly. Dashboards, models and reports work together so that decisions rest on facts</text>
      <text class="pw" x="25" y="52" font-style="italic">and growth is planned. Risk is reduced at every level of the company, from the board room to the shop</text>
      <text class="pw" x="25" y="58" font-style="italic">floor, with one clear view of the numbers.</text>
      <text class="ct" x="90" y="100" text-anchor="middle">Chart Title</text>
      <g class="ax" text-anchor="end">
        <text x="19" y="113">6</text><text x="19" y="122.6">5</text><text x="19" y="132.2">4</text><text x="19" y="141.8">3</text>
        <text x="19" y="151.4">2</text><text x="19" y="161">1</text><text x="19" y="170.6">0</text>
      </g>
      <line x1="24" y1="169" x2="160" y2="169" stroke="#ccc" stroke-width=".5"/>
      <g>
        <rect x="32" y="127" width="5" height="42" fill="var(--red)"/><rect x="38" y="146" width="5" height="23" fill="var(--charcoal)"/><rect x="44" y="150" width="5" height="19" fill="#9a9a9a"/>
        <rect x="66" y="145" width="5" height="24" fill="var(--red)"/><rect x="72" y="124" width="5" height="45" fill="var(--charcoal)"/><rect x="78" y="150" width="5" height="19" fill="#9a9a9a"/>
        <rect x="100" y="135" width="5" height="34" fill="var(--red)"/><rect x="106" y="152" width="5" height="17" fill="var(--charcoal)"/><rect x="112" y="140" width="5" height="29" fill="#9a9a9a"/>
        <rect x="134" y="125" width="5" height="44" fill="var(--red)"/><rect x="140" y="140" width="5" height="29" fill="var(--charcoal)"/><rect x="146" y="120" width="5" height="49" fill="#9a9a9a"/>
      </g>
      <g class="ax" text-anchor="middle"><text x="41" y="178">Category 1</text><text x="75" y="178">Category 2</text><text x="109" y="178">Category 3</text><text x="143" y="178">Category 4</text></g>
      <rect x="45" y="185" width="3" height="3" fill="var(--red)"/><text class="ax" x="49.5" y="188">Series 1</text>
      <rect x="78" y="185" width="3" height="3" fill="var(--charcoal)"/><text class="ax" x="82.5" y="188">Series 2</text>
      <rect x="111" y="185" width="3" height="3" fill="#9a9a9a"/><text class="ax" x="115.5" y="188">Series 3</text>
      <g fill="var(--red)">
        <polygon points="185,91 196,97.5 196,110.5 185,117 174,110.5 174,97.5"/>
        <polygon points="185,133 196,139.5 196,152.5 185,159 174,152.5 174,139.5"/>
        <polygon points="185,175 196,181.5 196,194.5 185,201 174,194.5 174,181.5"/>
      </g>
      <path d="M181 101v7c0 1.5 8 1.5 8 0v-7" fill="none" stroke="#fff" stroke-width=".8"/><ellipse cx="185" cy="101" rx="4" ry="1.3" fill="none" stroke="#fff" stroke-width=".8"/>
      <path d="M181 141h6l2 2v9h-8z" fill="none" stroke="#fff" stroke-width=".8"/>
      <path d="M185 182l5 3-5 3-5-3zM180 188l5 3 5-3" fill="none" stroke="#fff" stroke-width=".8"/>
      <text class="itb" x="207" y="97">Your Title Here</text>
      <text class="sm" x="207" y="104">Short note on the figure and what it shows for the team this quarter.</text>
      <text class="sm" x="207" y="110">A second line explains the result in plain and simple words.</text>
      <text class="itb" x="207" y="139">Your Title Here</text>
      <text class="sm" x="207" y="146">Short note on the figure and what it shows for the team this quarter.</text>
      <text class="sm" x="207" y="152">A second line explains the result in plain and simple words.</text>
      <text class="itb" x="207" y="181">Your Title Here</text>
      <text class="sm" x="207" y="188">Short note on the figure and what it shows for the team this quarter.</text>
      <text class="sm" x="207" y="194">A second line explains the result in plain and simple words.</text>
      <rect x="0" y="216" width="400" height="9" fill="var(--black)"/>
      <text class="foot" x="10" y="222">KESTRELARC.NET</text>
      <text class="foot" x="390" y="222" text-anchor="end">31</text>
    </svg>
  </section>

  <!-- Slide: four numbered points -->
  <section class="slide c3 r1">
    <svg viewBox="0 0 400 225">
      <rect width="400" height="225" fill="#fff"/>
      <rect width="100" height="225" fill="var(--red)"/>
      <rect x="100" width="100" height="225" fill="var(--charcoal)"/>
      <text class="hd-w" x="12" y="19" font-size="12">YOUR TITLE HERE</text>
      <rect x="311" y="5" width="83" height="12" fill="var(--black)"/>
      <text class="logo" x="352.5" y="13.3" text-anchor="middle">KESTREL ARC</text>
      <g>
        <circle cx="46" cy="52" r="10" fill="#fff"/><text class="num" x="46" y="53.6" text-anchor="middle" fill="var(--red)">01</text>
        <circle cx="151" cy="52" r="10" fill="#fff"/><text class="num" x="151" y="53.6" text-anchor="middle" fill="var(--charcoal)">02</text>
        <circle cx="46" cy="135" r="10" fill="#fff"/><text class="num" x="46" y="136.6" text-anchor="middle" fill="var(--red)">03</text>
        <circle cx="151" cy="135" r="10" fill="#fff"/><text class="num" x="151" y="136.6" text-anchor="middle" fill="var(--charcoal)">04</text>
      </g>
      <g text-anchor="middle">
        <text class="pw-t" x="48" y="77">TITLE GOES HERE</text>
        <text class="pw-s" x="48" y="87">Short text on the point</text>
        <text class="pw-s" x="48" y="92">and what it means for</text>
        <text class="pw-s" x="48" y="97">the team.</text>
        <text class="pw-t" x="151" y="77">TITLE GOES HERE</text>
        <text class="pw-s" x="151" y="87">Short text on the point</text>
        <text class="pw-s" x="151" y="92">and what it means for</text>
        <text class="pw-s" x="151" y="97">the team.</text>
        <text class="pw-t" x="48" y="160">TITLE GOES HERE</text>
        <text class="pw-s" x="48" y="170">Short text on the point</text>
        <text class="pw-s" x="48" y="175">and what it means for</text>
        <text class="pw-s" x="48" y="180">the team.</text>
        <text class="pw-t" x="151" y="160">TITLE GOES HERE</text>
        <text class="pw-s" x="151" y="170">Short text on the point</text>
        <text class="pw-s" x="151" y="175">and what it means for</text>
        <text class="pw-s" x="151" y="180">the team.</text>
      </g>
      <text class="p" x="214" y="48">Kestrel Arc turns complex data into simple insight for</text>
      <text class="p" x="214" y="54">leaders who need clear answers fast. Dashboards and</text>
      <text class="p" x="214" y="60">reports work together so decisions rest on facts and</text>
      <text class="p" x="214" y="66">growth is planned with care.</text>
      <text class="p" x="214" y="78">Risk is reduced at every level of the company, from the</text>
      <text class="p" x="214" y="84">board room to the shop floor.</text>
      <circle cx="244" cy="144" r="13" fill="var(--black)"/>
      <rect x="239" y="139" width="9" height="7" fill="none" stroke="#fff" stroke-width=".9"/><rect x="241" y="141" width="9" height="7" fill="none" stroke="#fff" stroke-width=".9"/>
      <circle cx="244" cy="181" r="13" fill="var(--red)"/>
      <rect x="239" y="176" width="9" height="7" fill="none" stroke="#fff" stroke-width=".9"/><rect x="241" y="178" width="9" height="7" fill="none" stroke="#fff" stroke-width=".9"/>
      <text class="sm" x="268" y="143">Short note on the figure shown</text>
      <text class="sm" x="268" y="148">with clear plain words.</text>
      <text class="sm" x="268" y="180">Short note on the figure shown</text>
      <text class="sm" x="268" y="185">with clear plain words.</text>
      <rect x="0" y="216" width="400" height="9" fill="var(--black)"/>
      <text class="foot" x="210" y="222">KESTRELARC.NET</text>
      <text class="foot" x="390" y="222" text-anchor="end">29</text>
    </svg>
  </section>

  <!-- Slide: system data display -->
  <section class="slide c1 r2">
    <svg viewBox="0 0 400 225">
      <defs>
        <linearGradient id="deviceTone" x1="0" y1="0" x2="0" y2="1">
          <stop offset="0" stop-color="#e9e9e9"/><stop offset="1" stop-color="#b9b9b9"/>
        </linearGradient>
      </defs>
      <rect width="400" height="225" fill="#fff"/>
      <rect x="0" y="9" width="4" height="11" fill="var(--red)"/>
      <text class="hd" x="11" y="18">SYSTEM DATA DISPLAY</text>
      <text class="sub" x="11" y="26">Enter your subtitle here</text>
      <rect x="311" y="5" width="83" height="12" fill="var(--black)"/>
      <text class="logo" x="352.5" y="13.3" text-anchor="middle">KESTREL ARC</text>
      <text class="p" x="25" y="45">Kestrel Arc turns complex data into simple insight for leaders who need clear answers fast, and helps every team see the business</text>
      <text class="p" x="25" y="52">plainly. Dashboards, models and reports work together so that decisions rest on facts and risk is reduced.</text>
      <rect x="58" y="78" width="288" height="120" rx="4" fill="url(#deviceTone)" role="img" aria-label="Laptop, tablet and phone showing a candlestick chart"/>
      <rect x="124" y="86" width="160" height="95" fill="#fff"/>
      <text class="ct" x="204" y="99" text-anchor="middle">Chart Title</text>
      <g class="ax" text-anchor="end">
        <text x="134" y="112">80</text><text x="134" y="123">60</text><text x="134" y="134">40</text><text x="134" y="145">20</text><text x="134" y="156">0</text>
      </g>
      <g stroke="#ddd" stroke-width=".4"><line x1="137" y1="111" x2="275" y2="111"/><line x1="137" y1="122" x2="275" y2="122"/><line x1="137" y1="133" x2="275" y2="133"/><line x1="137" y1="144" x2="275" y2="144"/><line x1="137" y1="155" x2="275" y2="155"/></g>
      <line x1="171" y1="124" x2="171" y2="139" stroke="#333" stroke-width=".6"/>
      <rect x="164" y="128" width="14" height="7" fill="#3a3a3a"/>
      <line x1="237" y1="134" x2="237" y2="148" stroke="#333" stroke-width=".6"/>
      <rect x="230" y="137" width="14" height="7" fill="#3a3a3a"/>
      <g class="ax" text-anchor="middle"><text x="171" y="163">1/8/2002</text><text x="237" y="163">1/9/2002</text></g>
      <g class="ax" text-anchor="middle"><text x="170" y="172">Open</text><text x="188" y="172">High</text><text x="206" y="172">Low</text><text x="224" y="172">Close</text></g>
      <rect x="0" y="216" width="400" height="9" fill="var(--black)"/>
      <text class="foot" x="10" y="222">KESTRELARC.NET</text>
      <text class="foot" x="390" y="222" text-anchor="end">64</text>
    </svg>
  </section>

  <!-- Slide: hexagon cluster -->
  <section class="slide c2 r2">
    <svg viewBox="0 0 400 225">
      <defs>
        <polygon id="hex" points="0,-19 16.5,-9.5 16.5,9.5 0,19 -16.5,9.5 -16.5,-9.5"/>
      </defs>
      <rect width="400" height="225" fill="#fff"/>
      <rect width="110" height="225" fill="var(--red-soft)"/>
      <g text-anchor="middle" class="pw">
        <text x="55" y="38">Kestrel Arc turns complex data into</text>
        <text x="55" y="49">simple insight for leaders who need</text>
        <text x="55" y="60">clear answers fast. Dashboards and</text>
        <text x="55" y="71">reports work together so decisions</text>
        <text x="55" y="82">rest on facts and growth is planned</text>
        <text x="55" y="93">with care, and risk is reduced at</text>
        <text x="55" y="104">every level.</text>
        <text x="55" y="126">Kestrel Arc turns complex data into</text>
        <text x="55" y="137">simple insight for leaders who need</text>
        <text x="55" y="148">clear answers fast. Dashboards and</text>
        <text x="55" y="159">reports work together so decisions</text>
        <text x="55" y="170">rest on facts and growth is planned</text>
        <text x="55" y="181">with care, and risk is reduced at</text>
        <text x="55" y="192">every level.</text>
      </g>
      <text class="hd" x="118" y="14">YOUR TITLE HERE</text>
      <text class="sub" x="120" y="22">Enter your subtitle here</text>
      <rect x="311" y="5" width="83" height="12" fill="var(--black)"/>
      <text class="logo" x="352.5" y="13.3" text-anchor="middle">KESTREL ARC</text>
      <text class="p" x="122" y="48">Kestrel Arc turns complex data into simple insight for leaders who need clear answers fast and sees</text>
      <text class="p" x="122" y="56">the business plainly. Dashboards and reports work together so decisions rest on facts.</text>
      <use href="#hex" x="230" y="101" fill="var(--red)"/>
      <use href="#hex" x="270" y="101" fill="var(--black)"/>
      <use href="#hex" x="210" y="136" fill="var(--black)"/>
      <use href="#hex" x="250" y="136" fill="#fff" stroke="#ccc" stroke-width=".6"/>
      <use href="#hex" x="290" y="136" fill="var(--red)"/>
      <use href="#hex" x="230" y="171" fill="var(--red)"/>
      <use href="#hex" x="270" y="171" fill="var(--black)"/>
      <text class="logo-dark" x="250" y="137" text-anchor="middle" style="font-size:2.5px">KESTREL ARC</text>
      <path d="M224 106h12M225.5 105v-4M228.5 105v-6M231.5 105v-3M234.5 105v-5" stroke="#fff" stroke-width="1.4"/>
      <circle cx="270" cy="101" r="4" fill="none" stroke="#fff" stroke-width="1.6" stroke-dasharray="1.8 1.3"/><circle cx="270" cy="101" r="1.6" fill="#fff"/>
      <path d="M210 132l5 3-5 3-5-3zM205 138l5 3 5-3" fill="none" stroke="#fff" stroke-width="1"/>
      <path d="M286 131h6l2 2v8h-8z" fill="none" stroke="#fff" stroke-width=".9"/><path d="M288 139v-3M290 139v-4M292 139v-2" stroke="#fff" stroke-width=".9"/>
      <rect x="225" y="167" width="10" height="7" fill="none" stroke="#fff" stroke-width=".9"/><path d="M227 172v-2M229 172v-3M231 172v-1.5M233 172v-3" stroke="#fff" stroke-width=".8"/>
      <path d="M265 176l3-4 3 2 4-5M264 177h12" fill="none" stroke="#fff" stroke-width="1.1"/>
      <g text-anchor="middle">
        <text class="it-s" x="153" y="95">Title Goes Here</text>
        <text class="sm" x="153" y="101">Suitable for all categories business</text>
        <text class="sm" x="153" y="106">and personal presentation.</text>
        <text class="it-s" x="153" y="134">Title Goes Here</text>
        <text class="sm" x="153" y="140">Suitable for all categories business</text>
        <text class="sm" x="153" y="145">and personal presentation.</text>
        <text class="it-s" x="153" y="170">Title Goes Here</text>
        <text class="sm" x="153" y="176">Suitable for all categories business</text>
        <text class="sm" x="153" y="181">and personal presentation.</text>
        <text class="it-s" x="346" y="95">Title Goes Here</text>
        <text class="sm" x="346" y="101">Suitable for all categories business</text>
        <text class="sm" x="346" y="106">and personal presentation.</text>
        <text class="it-s" x="346" y="131">Title Goes Here</text>
        <text class="sm" x="346" y="137">Suitable for all categories business</text>
        <text class="sm" x="346" y="142">and personal presentation.</text>
        <text class="it-s" x="346" y="170">Title Goes Here</text>
        <text class="sm" x="346" y="176">Suitable for all categories business</text>
        <text class="sm" x="346" y="181">and personal presentation.</text>
      </g>
      <rect x="110" y="216" width="290" height="9" fill="var(--black)"/>
      <text class="foot" x="118" y="222">KESTRELARC.NET</text>
    </svg>
  </section>

  <!-- Slide: half donut with titles -->
  <section class="slide c3 r2">
    <svg viewBox="0 0 400 225">
      <rect width="400" height="225" fill="#fff"/>
      <rect width="160" height="225" fill="var(--navy)"/>
      <text class="hd-w" x="10" y="19" font-size="11.5">TITLE HERE</text>
      <text class="pw" x="18" y="26" style="font-size:2.6px">Enter your subtitle here</text>
      <g class="pw" font-style="italic">
        <text x="16" y="52">Kestrel Arc turns complex data into simple</text>
        <text x="16" y="62">insight for leaders who need clear answers</text>
        <text x="16" y="72">fast. Dashboards, models and reports work</text>
        <text x="16" y="82">together so that decisions rest on facts</text>
        <text x="16" y="92">and growth is planned with care.</text>
        <text x="16" y="115">Risk is reduced at every level of the firm,</text>
        <text x="16" y="125">from the board room to the shop floor,</text>
        <text x="16" y="135">with one clear view of the numbers and</text>
        <text x="16" y="145">a shared plan that every team can read</text>
        <text x="16" y="155">and act on each week. Data becomes a</text>
        <text x="16" y="165">simple story with a clear next step for</text>
        <text x="16" y="175">leaders, owners and analysts.</text>
      </g>
      <rect x="311" y="5" width="83" height="12" fill="var(--black)"/>
      <text class="logo" x="352.5" y="13.3" text-anchor="middle">KESTREL ARC</text>
      <path d="M160 115L160 45A70 70 0 0 1 220.6 80Z" fill="#e2364b"/>
      <path d="M160 115L220.6 80A70 70 0 0 1 220.6 150Z" fill="#2f6d8a"/>
      <path d="M160 115L220.6 150A70 70 0 0 1 190 178Z" fill="#3aa8a8"/>
      <path d="M160 115L190 178A70 70 0 0 1 160 185Z" fill="#f2c12e"/>
      <circle cx="160" cy="115" r="22" fill="#fff"/>
      <text class="logo-dark" x="160" y="116.2" text-anchor="middle" style="font-size:3.2px">KESTREL ARC</text>
      <rect x="172" y="65" width="10" height="7" fill="none" stroke="#fff" stroke-width=".9"/><path d="M174 70v-2M176 70v-3M178 70v-1M180 70v-3" stroke="#fff" stroke-width=".7"/>
      <path d="M193 102h10M194.5 101v-4M197 101v-6M199.5 101v-3M202 101v-5" stroke="#fff" stroke-width="1.2"/>
      <path d="M197 134l5 3-5 3-5-3zM192 140l5 3 5-3" fill="none" stroke="#fff" stroke-width=".9"/>
      <path d="M173 157h6l2 2v8h-8z" fill="none" stroke="#fff" stroke-width=".8"/>
      <g fill="none" stroke="#555" stroke-width=".5" stroke-dasharray="1 1">
        <path d="M208 57l10-10h35"/><path d="M226 88h52"/><path d="M226 142h52"/><path d="M208 175l10 10h35"/>
      </g>
      <g fill="#555"><circle cx="208" cy="57" r="1"/><circle cx="226" cy="88" r="1"/><circle cx="226" cy="142" r="1"/><circle cx="208" cy="175" r="1"/></g>
      <text class="it" x="257" y="41">Your Title Here</text><text class="sm" x="257" y="48">Short note on the figure shown</text><text class="sm" x="257" y="53">with clear plain words.</text>
      <text class="it" x="284" y="84">Your Title Here</text><text class="sm" x="284" y="91">Short note on the figure shown</text><text class="sm" x="284" y="96">with clear plain words.</text>
      <text class="it" x="284" y="139">Your Title Here</text><text class="sm" x="284" y="146">Short note on the figure shown</text><text class="sm" x="284" y="151">with clear plain words.</text>
      <text class="it" x="257" y="187">Your Title Here</text><text class="sm" x="257" y="194">Short note on the figure shown</text><text class="sm" x="257" y="199">with clear plain words.</text>
      <rect x="160" y="216" width="240" height="9" fill="var(--black)"/>
      <text class="foot" x="210" y="222">KESTRELARC.NET</text>
      <text class="foot" x="390" y="222" text-anchor="end">34</text>
    </svg>
  </section>

  <!-- Slide: tree map -->
  <section class="slide c1 r3">
    <svg viewBox="0 0 400 225">
      <rect width="400" height="225" fill="#fff"/>
      <rect x="0" y="9" width="4" height="11" fill="var(--red)"/>
      <text class="hd" x="11" y="18">TREE STYLE DATA DISPLAY</text>
      <text class="sub" x="11" y="26">Enter your subtitle here</text>
      <rect x="311" y="5" width="83" height="12" fill="var(--black)"/>
      <text class="logo" x="352.5" y="13.3" text-anchor="middle">KESTREL ARC</text>
      <text class="ct" x="133" y="40" text-anchor="middle">Chart Title</text>
      <rect x="86" y="49" width="3" height="3" fill="var(--navy)"/><text class="ax" x="91" y="52">Branch 1</text>
      <rect x="120" y="49" width="3" height="3" fill="#c00000"/><text class="ax" x="125" y="52">Branch 2</text>
      <rect x="154" y="49" width="3" height="3" fill="#3a3a3a"/><text class="ax" x="159" y="52">Branch 3</text>
      <g stroke="#fff" stroke-width=".7">
        <rect x="4" y="61" width="52" height="107" fill="var(--navy)"/>
        <rect x="56" y="61" width="66" height="80" fill="var(--navy)"/>
        <rect x="56" y="141" width="42" height="27" fill="var(--navy)"/>
        <rect x="98" y="141" width="24" height="27" fill="var(--navy)"/>
        <rect x="4" y="168" width="50" height="37" fill="var(--navy)"/>
        <rect x="54" y="168" width="42" height="37" fill="var(--navy)"/>
        <rect x="96" y="168" width="26" height="37" fill="var(--navy)"/>
        <rect x="122" y="61" width="75" height="80" fill="#c00000"/>
        <rect x="122" y="141" width="75" height="23" fill="#c00000"/>
        <rect x="122" y="164" width="38" height="41" fill="#c00000"/>
        <rect x="160" y="164" width="37" height="41" fill="#c00000"/>
        <rect x="197" y="61" width="66" height="88" fill="#3a3a3a"/>
        <rect x="197" y="149" width="34" height="25" fill="#3a3a3a"/>
        <rect x="231" y="149" width="32" height="25" fill="#3a3a3a"/>
        <rect x="197" y="174" width="34" height="31" fill="#3a3a3a"/>
        <rect x="231" y="174" width="32" height="31" fill="#3a3a3a"/>
      </g>
      <g class="lf">
        <text x="6" y="67">Branch 1</text><text x="6" y="166">Leaf 5</text>
        <text x="58" y="139">Leaf 4</text><text x="58" y="166">Leaf 6</text><text x="100" y="166">Leaf 7</text>
        <text x="6" y="203">Leaf 1</text><text x="56" y="203">Leaf 3</text><text x="98" y="203">Leaf 2</text>
        <text x="124" y="67">Branch 2</text><text x="124" y="139">Leaf 11</text><text x="124" y="162">Leaf 10</text>
        <text x="124" y="203">Leaf 8</text><text x="162" y="203">Leaf 9</text>
        <text x="199" y="67">Branch 3</text><text x="199" y="147">Leaf 14</text><text x="199" y="172">Leaf 16</text>
        <text x="233" y="172">Leaf 15</text><text x="199" y="203">Leaf 13</text><text x="233" y="203">Leaf 12</text>
      </g>
      <circle cx="291" cy="75" r="8" fill="var(--red)" stroke="#f3b0b3" stroke-width="1.2"/><text class="num-s" x="291" y="76.4" text-anchor="middle">01</text>
      <circle cx="291" cy="124" r="8" fill="var(--red)" stroke="#f3b0b3" stroke-width="1.2"/><text class="num-s" x="291" y="125.4" text-anchor="middle">02</text>
      <circle cx="291" cy="170" r="8" fill="var(--red)" stroke="#f3b0b3" stroke-width="1.2"/><text class="num-s" x="291" y="171.4" text-anchor="middle">03</text>
      <text class="it" x="308" y="68">Title Goes Here</text><text class="sm" x="309" y="76">Suitable for all categories business</text><text class="sm" x="309" y="82">and personal presentation</text>
      <text class="it" x="308" y="117">Title Goes Here</text><text class="sm" x="309" y="125">Suitable for all categories business</text><text class="sm" x="309" y="131">and personal presentation</text>
      <text class="it" x="308" y="163">Title Goes Here</text><text class="sm" x="309" y="171">Suitable for all categories business</text><text class="sm" x="309" y="177">and personal presentation</text>
    </svg>
  </section>

  <!-- Slide: sunburst -->
  <section class="slide c2 r3">
    <svg viewBox="0 0 400 225">
      <rect width="400" height="225" fill="#fff"/>
      <rect x="0" y="9" width="4" height="11" fill="var(--red)"/>
      <text class="hd" x="11" y="18">SUN BURST STYLE DATA DISPLAY</text>
      <text class="sub" x="11" y="26">Enter your subtitle here</text>
      <rect x="311" y="5" width="83" height="12" fill="var(--black)"/>
      <text class="logo" x="352.5" y="13.3" text-anchor="middle">KESTREL ARC</text>
      <text class="ct" x="105" y="52" text-anchor="middle">Chart Title</text>
      <g transform="rotate(-90 105 125)" fill="none">
        <circle cx="105" cy="125" r="24" stroke="#8f8f8f" stroke-width="12"/>
        <circle cx="105" cy="125" r="24" stroke="#b4b4b4" stroke-width="12" stroke-dasharray="48 103"/>
        <circle cx="105" cy="125" r="24" stroke="#a2a2a2" stroke-width="12" stroke-dasharray="50 101" stroke-dashoffset="-50"/>
        <circle cx="105" cy="125" r="37.5" stroke="#9c9c9c" stroke-width="14"/>
        <circle cx="105" cy="125" r="37.5" stroke="#c5c5c5" stroke-width="14" stroke-dasharray="40 196" stroke-dashoffset="-10"/>
        <circle cx="105" cy="125" r="37.5" stroke="#7d7d7d" stroke-width="14" stroke-dasharray="45 191" stroke-dashoffset="-95"/>
        <circle cx="105" cy="125" r="37.5" stroke="#b0b0b0" stroke-width="14" stroke-dasharray="50 186" stroke-dashoffset="-165"/>
        <circle cx="105" cy="125" r="52.5" stroke="#aaaaaa" stroke-width="14" stroke-dasharray="300 30"/>
        <circle cx="105" cy="125" r="52.5" stroke="#cfcfcf" stroke-width="14" stroke-dasharray="55 275" stroke-dashoffset="-20"/>
        <circle cx="105" cy="125" r="52.5" stroke="#8a8a8a" stroke-width="14" stroke-dasharray="60 270" stroke-dashoffset="-140"/>
        <circle cx="105" cy="125" r="52.5" stroke="#bdbdbd" stroke-width="14" stroke-dasharray="50 280" stroke-dashoffset="-230"/>
        <circle cx="105" cy="125" r="65" stroke="#c9c9c9" stroke-width="9" stroke-dasharray="90 60 120 139"/>
      </g>
      <g stroke="#fff" stroke-width=".8">
        <line x1="105" y1="107" x2="105" y2="55"/><line x1="123" y1="125" x2="175" y2="125"/>
        <line x1="105" y1="143" x2="105" y2="195"/><line x1="87" y1="125" x2="35" y2="125"/>
        <line x1="118" y1="112" x2="154" y2="76"/><line x1="92" y1="138" x2="56" y2="174"/>
        <line x1="118" y1="138" x2="154" y2="174"/><line x1="92" y1="112" x2="56" y2="76"/>
      </g>
      <circle cx="105" cy="125" r="17" fill="#fff"/>
      <g class="ax-s">
        <text x="44" y="120">Leaf</text><text x="45" y="125">11</text>
        <text x="62" y="117">Stem</text><text x="64" y="122">4</text>
        <text x="82" y="113">Branc</text><text x="84" y="118">h 2</text>
        <text x="120" y="112">Branc</text><text x="122" y="117">h 1</text>
        <text x="148" y="112">Leaf 4</text>
        <text x="96" y="160">Stem</text><text x="104" y="153">6</text>
      </g>
      <text class="it" x="290" y="70" text-anchor="middle">Title Goes Here</text>
      <g class="p" text-anchor="middle">
        <text x="290" y="83">Kestrel Arc turns complex data into simple insight for leaders</text>
        <text x="290" y="91">who need clear answers fast and see the business plainly.</text>
        <text x="290" y="99">Dashboards, models and reports work together so that every</text>
        <text x="290" y="107">decision rests on facts, growth is planned with care and</text>
        <text x="290" y="115">risk is reduced across the company, from the board room</text>
        <text x="290" y="123">to the shop floor, with one clear and shared view of the</text>
        <text x="290" y="131">numbers for all.</text>
      </g>
      <circle cx="233" cy="162" r="8" fill="#6b6b6b"/><circle cx="233" cy="162" r="3" fill="none" stroke="#fff" stroke-width="1.4" stroke-dasharray="1.4 1"/>
      <circle cx="342" cy="162" r="8" fill="#9a9a9a"/><ellipse cx="342" cy="159" rx="3" ry="1" fill="none" stroke="#fff" stroke-width=".7"/><path d="M339 159v5c0 1.3 6 1.3 6 0v-5" fill="none" stroke="#fff" stroke-width=".7"/>
      <g text-anchor="middle">
        <text class="it" x="233" y="181">Your Title Here</text><text class="sm" x="233" y="187">Short note on the</text><text class="sm" x="233" y="192">figure in plain words</text>
        <text class="it" x="342" y="181">Your Title Here</text><text class="sm" x="342" y="187">Short note on the</text><text class="sm" x="342" y="192">figure in plain words</text>
      </g>
    </svg>
  </section>

  <!-- Slide: waterfall -->
  <section class="slide c3 r3">
    <svg viewBox="0 0 400 225">
      <rect width="400" height="225" fill="#fff"/>
      <rect x="0" y="9" width="4" height="11" fill="var(--red)"/>
      <text class="hd" x="11" y="18">WATER FALL DATA DISPLAY</text>
      <text class="sub" x="11" y="26">Enter your subtitle here</text>
      <rect x="311" y="5" width="83" height="12" fill="var(--black)"/>
      <text class="logo" x="352.5" y="13.3" text-anchor="middle">KESTREL ARC</text>
      <text class="ct" x="260" y="43" text-anchor="middle">Chart Title</text>
      <rect x="217" y="51" width="3" height="3" fill="#2f6fb3"/><text class="ax" x="222" y="54">Increase</text>
      <rect x="249" y="51" width="3" height="3" fill="#e07b2a"/><text class="ax" x="254" y="54">Decrease</text>
      <rect x="286" y="51" width="3" height="3" fill="#888"/><text class="ax" x="291" y="54">Total</text>
      <g class="ax" text-anchor="end">
        <text x="146" y="66">180</text><text x="146" y="78.8">160</text><text x="146" y="91.6">140</text><text x="146" y="104.4">120</text>
        <text x="146" y="117.2">100</text><text x="146" y="130">80</text><text x="146" y="142.8">60</text><text x="146" y="155.6">40</text>
        <text x="146" y="168.4">20</text><text x="146" y="181.2">0</text>
      </g>
      <line x1="150" y1="180" x2="395" y2="180" stroke="#ccc" stroke-width=".5"/>
      <rect x="155" y="116" width="32" height="64" fill="#6b6566"/>
      <rect x="205" y="103.2" width="32" height="12.8" fill="#1f2b3a"/>
      <rect x="253" y="71.2" width="32" height="32" fill="#160808"/>
      <rect x="301" y="71.2" width="32" height="25.6" fill="#c00000"/>
      <rect x="349" y="96.8" width="32" height="83.2" fill="#6b6566"/>
      <g class="ax" text-anchor="middle" fill="#333">
        <text x="171" y="114">100</text><text x="221" y="101">20</text><text x="269" y="69">50</text><text x="317" y="101">-40</text><text x="365" y="95">130</text>
      </g>
      <g class="ax" text-anchor="middle"><text x="171" y="190">Category 1</text><text x="221" y="190">Category 2</text><text x="269" y="190">Category 3</text><text x="317" y="190">Category 4</text><text x="365" y="190">Category 5</text></g>
      <circle cx="29" cy="75" r="8" fill="var(--red)" stroke="#f3b0b3" stroke-width="1.2"/><text class="num-s" x="29" y="76.4" text-anchor="middle">01</text>
      <circle cx="29" cy="124" r="8" fill="var(--red)" stroke="#f3b0b3" stroke-width="1.2"/><text class="num-s" x="29" y="125.4" text-anchor="middle">02</text>
      <circle cx="29" cy="170" r="8" fill="var(--red)" stroke="#f3b0b3" stroke-width="1.2"/><text class="num-s" x="29" y="171.4" text-anchor="middle">03</text>
      <text class="it" x="47" y="68">Title Goes Here</text><text class="sm" x="48" y="76">Suitable for all categories business</text><text class="sm" x="48" y="82">and personal presentation</text>
      <text class="it" x="47" y="117">Title Goes Here</text><text class="sm" x="48" y="125">Suitable for all categories business</text><text class="sm" x="48" y="131">and personal presentation</text>
      <text class="it" x="47" y="163">Title Goes Here</text><text class="sm" x="48" y="171">Suitable for all categories business</text><text class="sm" x="48" y="177">and personal presentation</text>
    </svg>
  </section>
</main>
</body>
</html>
```